Serene Spiritual Website Wanted for World Wide Organisation

We need a serene, clean web design for our organisation that works around the world.

What We Do
We aim to bring life into synergy across the world. We inspire, motivate, synchronise, and harmonise. We work with energy which is essential to all of life (environmental, human & animal). Our website must depict the spiritual element of being innately natural and reflect animism.

We have included a PDF attachment with details of the structure, navigation, and some websites for ideas/reference. The logo is also attached.
Updates

Target Market(s)

Anyone over 18yrs looking for answers to life's big questions or looking to develop themselves

Industry/Entity Type

Spiritual/wellbeing/Self Development

Number of Pages Required

5+ page

Requirements
Must have
• It must be serene and natural looking, it must incorporate the logo.
Nice to have
• We have included a Powerpoint document which may help you understand what we need, it is just an idea for structure and style, it is not set in stone so feel free to be as creative as you like!
Should not have
• Not clinical.

```html
<!DOCTYPE html>
<html lang="en">
<head>
<meta charset="utf-8">
<title>Lumenfold</title>
<link href="https://fonts.googleapis.com/css2?family=Ubuntu:wght@400;500;700&family=Open+Sans:wght@400;600;700&display=swap" rel="stylesheet">
<style>
:root{
  --purple:#3f3b6c;
  --purple-deep:#2c2953;
  --gold:#e3d184;
  --ink:#23213f;
  --muted:#6b6a80;
  --line:#e6e5ee;
  --white:#ffffff;
}
*{box-sizing:border-box;margin:0;padding:0}
html,body{width:1200px;height:4676px;overflow:hidden}
body{position:relative;background:var(--white);font-family:"Open Sans",sans-serif;color:var(--ink)}
.abs{position:absolute}
h1,h2,h3,.brand{font-family:"Ubuntu",sans-serif}
.label{font-size:16px;font-weight:700;letter-spacing:1px;text-transform:uppercase;color:var(--ink)}
.title{font-size:40px;font-weight:700;line-height:48px;color:var(--ink)}
.btn{display:flex;align-items:center;justify-content:center;background:var(--gold);color:var(--ink);border-radius:24px;font-size:15px;font-weight:600}
.photo{position:absolute}
p.body{font-size:17px;line-height:26px;color:var(--muted)}

/* header */
.top-band{left:0;top:0;width:1200px;height:580px;background:var(--purple)}
.nav{top:48px;display:flex;gap:0;font-size:15px;font-weight:600;color:var(--white);letter-spacing:1px}
.nav span{padding:0 28px;border-right:1px solid rgba(255,255,255,.5)}
.nav span:last-child{border-right:none}
.logo{display:flex;flex-direction:column;align-items:center;gap:8px}
.logo .mark{width:40px;height:40px;border-radius:50%;background:var(--gold)}
.logo .brand{font-size:18px;font-weight:500;color:var(--gold)}
.hero{left:140px;top:140px;width:980px;height:532px;background:radial-gradient(ellipse at 50% 30%,#5a5aa0 0%,#2a2550 45%,#120f25 100%)}
.hero h1{position:absolute;left:100px;width:780px;top:300px;text-align:center;color:var(--white);font-size:40px;line-height:52px;font-weight:700}
.hero .more{position:absolute;left:0;width:980px;top:462px;text-align:center;color:var(--white);font-size:14px;font-weight:600}
.hero .arrow{position:absolute;top:376px}

/* events */
.event-img{width:232px;height:220px}
.event-meta{font-size:15px;color:var(--ink)}
.event-title{font-size:22px;font-weight:700;line-height:28px;color:var(--ink)}
.event-text{font-size:15px;line-height:22px;color:var(--muted)}
.event-link{font-size:15px;color:var(--ink);display:flex;align-items:center;gap:10px}
.event-link::before{content:"";width:28px;height:1px;background:var(--ink)}

/* about */
.about-band{left:0;top:1552px;width:1200px;height:516px;background:var(--purple)}
.light{color:var(--white)}
.light-label{color:var(--white)}
.light-text{color:rgba(255,255,255,.8)}

/* accordion */
.acc{left:88px;width:500px;background:var(--white);box-shadow:0 4px 20px rgba(40,35,80,.12);border-radius:4px}
.acc .head{display:flex;justify-content:space-between;align-items:center;padding:0 22px;font-size:18px;font-weight:600;color:var(--ink)}

/* products */
.card{width:236px;height:384px;background:var(--white);box-shadow:0 4px 20px rgba(40,35,80,.12)}
.card .img{height:212px}
.card .name{position:absolute;left:20px;top:236px;font-size:18px;font-weight:700;color:var(--purple)}
.card .desc{position:absolute;left:20px;top:264px;width:196px;font-size:14px;line-height:20px;color:var(--muted)}
.card .price{position:absolute;left:20px;top:326px;font-size:30px;font-weight:700;color:var(--purple);font-family:"Ubuntu",sans-serif}
.card .cart{position:absolute;right:20px;top:334px}
.round{width:32px;height:32px;border-radius:50%;background:var(--purple);display:flex;align-items:center;justify-content:center}

/* footer */
.footer{left:0;top:4232px;width:1200px;height:444px;background:var(--purple)}
.rule{position:absolute;left:88px;width:1024px;height:1px;background:rgba(255,255,255,.25)}
.social{width:30px;height:30px;border-radius:50%;border:2px solid var(--white)}
</style>
</head>
<body>

<!-- Header -->
<div class="abs top-band"></div>
<nav class="abs nav" style="left:130px"><span>HOME</span><span>EVENTS</span><span>ABOUT</span></nav>
<div class="abs logo" style="left:530px;top:24px;width:140px"><div class="mark"></div><div class="brand">Lumenfold</div></div>
<nav class="abs nav" style="left:720px"><span>SYNERGISE</span><span>WISDOM</span><span>SHOP</span></nav>

<section class="abs hero" role="img" aria-label="Night sky full of stars above a figure meditating at the end of a long path">
  <h1>Three Thinks Cannot Be Long Hidden: The&nbsp;Sun,The Moon And The Truth</h1>
  <div class="more">Learn More</div>
  <svg class="arrow" style="left:4px" width="40" height="24"><path d="M36 12H6M14 4L6 12l8 8" stroke="#fff" stroke-width="2.5" fill="none"/></svg>
  <svg class="arrow" style="left:936px" width="40" height="24"><path d="M4 12h30M26 4l8 8-8 8" stroke="#fff" stroke-width="2.5" fill="none"/></svg>
  <svg class="abs" style="left:474px;top:492px" width="32" height="24"><path d="M4 4l12 8 12-8M4 12l12 8 12-8" stroke="var(--gold)" stroke-width="2.5" fill="none"/></svg>
</section>

<!-- Events -->
<div class="abs label" style="left:88px;top:820px">Events</div>
<h2 class="abs title" style="left:88px;top:848px;width:440px">Current Events And Workshops</h2>
<div class="abs btn" style="left:960px;top:828px;width:152px;height:48px">More Events</div>

<div class="photo event-img" style="left:88px;top:972px;background:linear-gradient(180deg,#f2b47e,#c98aa8 55%,#6d5c8a)" role="img" aria-label="Birds flying away from a broken chain at sunset"></div>
<div class="abs" style="left:344px;top:972px;width:240px">
  <div class="event-meta">📅 20 Aug &nbsp;|&nbsp; 8:00 am</div>
  <div class="event-title" style="margin-top:10px">Ut id neque sit amet risus tempor</div>
  <div class="event-text" style="margin-top:8px">Lorem ipsum dolor sit amet, consectetur adipiscing elit. Aliquam ne</div>
  <div class="event-link" style="margin-top:14px">More Details</div>
</div>
<div class="photo event-img" style="left:612px;top:972px;background:linear-gradient(180deg,#b9c4c9,#7f8a8c 55%,#4a4a45)" role="img" aria-label="Person sitting on a jetty looking over a calm lake"></div>
<div class="abs" style="left:872px;top:972px;width:240px">
  <div class="event-meta">📅 22 Aug &nbsp;|&nbsp; 8:00 am</div>
  <div class="event-title" style="margin-top:10px">Ut id neque sit amet risus tempor</div>
  <div class="event-text" style="margin-top:8px">Lorem ipsum dolor sit amet, consectetur adipiscing elit. Aliquam ne</div>
  <div class="event-link" style="margin-top:14px">More Details</div>
</div>

<div class="photo event-img" style="left:88px;top:1228px;background:linear-gradient(180deg,#e1a875,#a86d63 55%,#4a3342)" role="img" aria-label="Silhouette of a person meditating against a warm sunset"></div>
<div class="abs" style="left:344px;top:1228px;width:240px">
  <div class="event-meta">📅 26 Aug &nbsp;|&nbsp; 8:00 am</div>
  <div class="event-title" style="margin-top:10px">Ut id neque sit amet risus tempor</div>
  <div class="event-text" style="margin-top:8px">Lorem ipsum dolor sit amet, consectetur adipiscing elit. Aliquam ne</div>
  <div class="event-link" style="margin-top:14px">More Details</div>
</div>
<div class="photo event-img" style="left:612px;top:1228px;background:radial-gradient(circle at 50% 40%,#9fd6f5,#3c5c9a 55%,#1b1a35)" role="img" aria-label="Open book glowing with magical light"></div>
<div class="abs" style="left:872px;top:1228px;width:240px">
  <div class="event-meta">📅 28 Aug &nbsp;|&nbsp; 8:00 am</div>
  <div class="event-title" style="margin-top:10px">Ut id neque sit amet risus tempor</div>
  <div class="event-text" style="margin-top:8px">Lorem ipsum dolor sit amet, consectetur adipiscing elit. Aliquam ne</div>
  <div class="event-link" style="margin-top:14px">More Details</div>
</div>

<!-- About -->
<div class="abs about-band"></div>
<div class="photo" style="left:0;top:1552px;width:600px;height:516px;background:radial-gradient(ellipse at 45% 80%,#f0b070 0%,#7a5a8a 35%,#2d3466 70%,#151a3a)" role="img" aria-label="Silhouette of a woman meditating under a starry sky"></div>
<div class="abs label light-label" style="left:648px;top:1652px">About</div>
<h2 class="abs title light" style="left:648px;top:1680px;width:460px">Learn About Sunny Day</h2>
<p class="abs body light-text" style="left:648px;top:1784px;width:480px;font-size:16px;line-height:24px">Lorem ipsum dolor sit amet, consectetur adipiscing elit. Aliquam nec tellus interdum felis in dapibus pellentesque. Suspendisse non laoreet nibh, sed porta tellus quis ante laoreet commodo. Etiam consectetur massa eu luctus mollis. Aliquam consequat pellentesque erat</p>
<div class="abs btn" style="left:648px;top:1912px;width:148px;height:48px">Learn More</div>

<!-- Shop -->
<div class="abs label" style="left:88px;top:2168px">Shop</div>
<h2 class="abs title" style="left:88px;top:2196px;width:540px">We inspire, motivate, synchronise, and harmonise</h2>

<div class="abs acc" style="top:2340px;height:200px">
  <div class="head" style="height:64px">Malas <span style="font-size:22px">−</span></div>
  <p class="body" style="padding:0 22px;font-size:15px;line-height:22px">Lorem ipsum dolor sit amet, consectetur adipiscing elit. Aliquam nec tellus interdum felis in dapibus, accumsan ante. Lorem ipsum dolor sit</p>
  <div class="event-link" style="padding:12px 22px 0">More info</div>
</div>
<div class="abs acc" style="top:2572px;height:68px"><div class="head" style="height:68px">Art <span style="font-size:22px">+</span></div></div>
<div class="abs acc" style="top:2660px;height:68px"><div class="head" style="height:68px">Books <span style="font-size:22px">+</span></div></div>
<div class="abs acc" style="top:2748px;height:68px"><div class="head" style="height:68px">Synchronised Life <span style="font-size:22px">+</span></div></div>

<div class="photo" style="left:640px;top:2300px;width:520px;height:580px;background:radial-gradient(ellipse at 50% 45%,#3a2f8a 0%,#2b2670 35%,#e9e6f5 62%,#ffffff 80%)" role="img" aria-label="Illustration of a meditating figure with glowing chakra points"></div>

<!-- Meditation -->
<div class="abs" style="left:0;top:2912px;width:600px;height:560px;background:var(--purple)"></div>
<div class="abs label light-label" style="left:88px;top:3016px">Meditation</div>
<h2 class="abs title light" style="left:88px;top:3044px;width:480px">We work with energy which is essential to all of life</h2>
<p class="abs body light-text" style="left:88px;top:3188px;width:460px;font-size:16px;line-height:24px">Lorem ipsum dolor sit amet, consectetur adipiscing elit. Aliquam nec tellus interdum felis in dapibus pellentesque. Suspendisse non laoreet nibh, sed porta tellus quis ante laoreet commodo. Etiam consectetur massa eu luctus mollis. Aliquam consequat</p>
<div class="abs btn" style="left:88px;top:3316px;width:128px;height:48px">Learn More</div>
<div class="photo" style="left:600px;top:2912px;width:600px;height:560px;background:radial-gradient(circle at 50% 45%,#f7c27a 0%,#a05a3a 22%,#2a1a2a 45%,#0e0c18 100%)" role="img" aria-label="Person meditating before a glowing circular portal"></div>

<!-- Malas -->
<div class="abs label" style="left:0;width:1200px;top:3572px;text-align:center;font-size:14px">Malas</div>
<h2 class="abs title" style="left:0;width:1200px;top:3592px;text-align:center">Malas: yoga prayer bead necklace</h2>
<p class="abs body" style="left:400px;width:400px;top:3652px;text-align:center;font-size:15px;line-height:22px">Lorem ipsum dolor sit amet, consectetur adipiscing elit. Aliquam nec tellus interdum felis in dapibus</p>

<div class="abs card" style="left:88px;top:3728px"><div class="img" style="background:linear-gradient(160deg,#e8c8b4,#b98a78)" role="img" aria-label="Hands holding a mala bead necklace"></div><div class="name">Lorem Ipsum</div><div class="desc">Lorem ipsum dolor sit amet, consectetur adipiscing</div><div class="price">$90</div><svg class="cart" width="22" height="20"><path d="M1 2h4l3 11h10l3-8H7" stroke="var(--purple)" stroke-width="2" fill="none"/><circle cx="9" cy="17" r="2" fill="var(--purple)"/><circle cx="17" cy="17" r="2" fill="var(--purple)"/></svg></div>
<div class="abs card" style="left:348px;top:3728px"><div class="img" style="background:linear-gradient(160deg,#d9d3cc,#8f8073)" role="img" aria-label="Prayer beads held in folded hands"></div><div class="name">Lorem Ipsum</div><div class="desc">Lorem ipsum dolor sit amet, consectetur adipiscing</div><div class="price">$90</div><svg class="cart" width="22" height="20"><path d="M1 2h4l3 11h10l3-8H7" stroke="var(--purple)" stroke-width="2" fill="none"/><circle cx="9" cy="17" r="2" fill="var(--purple)"/><circle cx="17" cy="17" r="2" fill="var(--purple)"/></svg></div>
<div class="abs card" style="left:612px;top:3728px"><div class="img" style="background:linear-gradient(160deg,#c9b9a8,#6e5a4c)" role="img" aria-label="Wooden mala beads on a table"></div><div class="name">Lorem Ipsum</div><div class="desc">Lorem ipsum dolor sit amet, consectetur adipiscing</div><div class="price">$90</div><svg class="cart" width="22" height="20"><path d="M1 2h4l3 11h10l3-8H7" stroke="var(--purple)" stroke-width="2" fill="none"/><circle cx="9" cy="17" r="2" fill="var(--purple)"/><circle cx="17" cy="17" r="2" fill="var(--purple)"/></svg></div>
<div class="abs card" style="left:876px;top:3728px"><div class="img" style="background:linear-gradient(160deg,#d8b58c,#8a6a4a)" role="img" aria-label="Mala necklace with tassel held in hand"></div><div class="name">Lorem Ipsum</div><div class="desc">Lorem ipsum dolor sit amet, consectetur adipiscing</div><div class="price">$90</div><svg class="cart" width="22" height="20"><path d="M1 2h4l3 11h10l3-8H7" stroke="var(--purple)" stroke-width="2" fill="none"/><circle cx="9" cy="17" r="2" fill="var(--purple)"/><circle cx="17" cy="17" r="2" fill="var(--purple)"/></svg></div>

<div class="abs round" style="left:72px;top:3916px"><svg width="12" height="12"><path d="M8 1L3 6l5 5" stroke="#fff" stroke-width="2" fill="none"/></svg></div>
<div class="abs round" style="left:1096px;top:3916px"><svg width="12" height="12"><path d="M4 1l5 5-5 5" stroke="#fff" stroke-width="2" fill="none"/></svg></div>

<!-- Footer -->
<footer class="abs footer">
  <nav class="abs nav" style="left:130px;top:116px"><span>HOME</span><span>EVENTS</span><span>ABOUT</span></nav>
  <div class="abs logo" style="left:530px;top:64px;width:140px"><div class="mark"></div><div class="brand">Lumenfold</div></div>
  <nav class="abs nav" style="left:720px;top:116px"><span>SYNERGISE</span><span>WISDOM</span><span>SHOP</span></nav>
  <div class="rule" style="top:188px"></div>
  <div class="abs" style="left:0;width:1200px;top:224px;display:flex;justify-content:center;gap:60px;color:var(--white);font-size:15px;font-weight:600">
    <span style="display:flex;align-items:center;gap:10px"><svg width="18" height="18"><path d="M4 1l3 4-2 2c1 3 3 5 6 6l2-2 4 3-2 3C8 17 1 10 1 3z" fill="#fff"/></svg>Phone: (01) 555 0147</span>
    <span style="display:flex;align-items:center;gap:10px"><svg width="20" height="16"><rect x="1" y="1" width="18" height="14" fill="none" stroke="#fff" stroke-width="2"/><path d="M1 2l9 7 9-7" stroke="#fff" stroke-width="2" fill="none"/></svg>Email: hello@lumenfold.org</span>
  </div>
  <div class="rule" style="top:280px"></div>
  <div class="abs" style="left:0;width:1200px;top:308px;text-align:center;color:var(--white);font-size:15px;font-weight:600">Copyright © <span style="color:var(--gold)">Lumenfold</span> 2022, All Rights Reserved.</div>
  <div class="abs" style="left:0;width:1200px;top:364px;display:flex;justify-content:center;gap:14px">
    <div class="social"></div><div class="social"></div><div class="social"></div><div class="social"></div>
  </div>
</footer>

</body>
</html>
```